Pebble Lane real estate investment company needs a poster design

We would like a poster design size 18 x 24.
Poster wording -
I WANT TO BUY YOUR ( finish with logo) logo uploaded
website- www.pebblelane-homes.example
phone # 555-217-8843 ( color red for the phone number)
we would like to see the poster on 2 different backgrounds
Yellow background
White background
horizontal

```html
<!DOCTYPE html>
<html lang="en">
<head>
<meta charset="utf-8">
<title>Pebble Lane — I Want To Buy Your House</title>
<link rel="stylesheet" href="https://fonts.googleapis.com/css2?family=Montserrat:wght@600;700;800&display=swap">
<style>
  :root {
    --red: #e21f26;
    --yellow: #ffed00;
    --white: #ffffff;
    --black: #000000;
  }
  html, body {
    margin: 0;
    padding: 0;
    width: 1200px;
    height: 900px;
    overflow: hidden;
    background: var(--white);
  }
  .poster {
    display: block;
    width: 1200px;
    height: 900px;
    font-family: "Montserrat", Arial, sans-serif;
  }
  .bg-red { fill: var(--red); }
  .bg-yellow { fill: var(--yellow); }
  .stripe-white { fill: var(--white); }
  .stripe-black { fill: var(--black); }
  .headline-want {
    fill: var(--white);
    font-weight: 600;
    font-size: 283px;
    filter: drop-shadow(4px 8px 0 var(--black));
  }
  .headline-buy {
    fill: var(--red);
    font-weight: 700;
    font-size: 177px;
  }
  .brand-name {
    fill: var(--black);
    font-weight: 800;
    font-size: 118px;
  }
  .brand-web {
    fill: var(--black);
    font-weight: 700;
    font-size: 42px;
  }
  .phone-badge { fill: var(--yellow); }
  .phone-icon { fill: var(--black); }
  .phone-number {
    fill: var(--white);
    font-weight: 700;
    font-size: 178px;
  }
</style>
</head>
<body>
<svg class="poster" viewBox="0 0 1200 900" xmlns="http://www.w3.org/2000/svg">
  <rect class="bg-red" x="0" y="0" width="1200" height="900"/>
  <path class="bg-yellow" d="M0,64 C90,140 200,210 304,236 C400,258 550,248 664,232 C800,212 900,192 1000,192 C1100,192 1150,205 1200,220 L1200,900 L0,900 Z"/>

  <path class="stripe-white" d="M0,684 C160,600 300,590 420,596 C620,606 900,676 1200,638 L1200,900 L0,900 Z"/>
  <path class="stripe-black" d="M0,697 C160,614 300,604 420,610 C620,620 900,692 1200,652 L1200,900 L0,900 Z"/>
  <path class="bg-red" d="M0,834 C130,730 330,642 560,648 C780,654 980,722 1200,680 L1200,900 L0,900 Z"/>

  <text class="headline-want" x="22" y="222" textLength="1154" lengthAdjust="spacingAndGlyphs">I WANT</text>
  <text class="headline-buy" x="28" y="406" textLength="1136" lengthAdjust="spacingAndGlyphs">TO BUY YOUR</text>

  <text class="brand-name" x="342" y="552" textLength="820" lengthAdjust="spacingAndGlyphs">Pebble Lane</text>
  <text class="brand-web" x="1164" y="606" text-anchor="end">www.pebblelane-homes.example</text>

  <circle class="phone-badge" cx="124" cy="780" r="79"/>
  <path class="phone-icon" d="M95,728 L103,723 L120,748 L113,754 C110,756 109,760 111,767 C114,779 123,791 133,798 C138,801 142,802 145,800 L152,795 L166,817 C162,822 156,826 149,824 C130,819 111,802 99,781 C89,763 86,742 95,728 Z"/>

  <text class="phone-number" x="236" y="856" textLength="924" lengthAdjust="spacingAndGlyphs">555-217-8843</text>
</svg>
</body>
</html>
```